Visitenkarten-Design für Unternehmensberatung
Zielgruppe
Unternehmensberatung, Auswanderungsberatung und Firmengründung in Dubai. Wir suchen ein modernes Design. unserer Zielgruppe sind deutschsprachige Unternehmer
Aufgabenstellung
Lukas Brandtner - CEO
Adresse: Harbor Crest Park, Building C7, Dubai, VAE
EMail: kontakt@terravia-plan.de
WhatsApp: +49 1764093217
Mobil: +971 563841072
www.terravia-plan.de
(Instagram: https://www.instagram.com/terravia.plan/)

```html
<!DOCTYPE html>
<html lang="de">
<head>
<meta charset="utf-8">
<title>Terravia Plan – Visitenkarte</title>
<link rel="stylesheet" href="https://fonts.googleapis.com/css2?family=Montserrat:wght@500;600;700&family=Arimo:wght@400&display=swap">
<style>
  :root {
    --page: #fefefe;
    --card: #ecebe9;
    --panel: #000000;
    --stripe-dark: #565753;
    --stripe-light: #dcdad7;
    --logo-disc: #d6d6d6;
    --ink: #161616;
    --white: #ffffff;
  }
  * { margin: 0; padding: 0; box-sizing: border-box; }
  html, body {
    width: 1200px; height: 1200px; overflow: hidden;
    background: var(--page);
  }
  body { position: relative; font-family: "Montserrat", sans-serif; }

  .card {
    position: absolute;
    left: 355px;
    width: 499px;
    height: 285px;
    background: var(--card);
    box-shadow: 4px 4px 6px rgba(0, 0, 0, 0.25);
    overflow: hidden;
  }
  .card--front { top: 292px; }
  .card--back  { top: 630px; }

  .stripes {
    position: absolute; left: 0; top: 0;
    width: 100%; height: 100%;
  }
  .stripe--dark  { fill: var(--stripe-dark); }
  .stripe--light { fill: var(--stripe-light); }

  .brand {
    position: absolute;
    display: flex; align-items: center;
  }
  .brand__disc {
    border-radius: 50%;
    background: var(--logo-disc);
    flex: none;
  }
  .brand__name {
    font-weight: 700;
    color: var(--ink);
    white-space: nowrap;
    letter-spacing: 0.2px;
  }
  .card--front .brand { left: 31px; top: 113px; gap: 6px; }
  .card--front .brand__disc { width: 31px; height: 31px; }
  .card--front .brand__name { font-size: 13px; }

  .card--back .brand { left: 89px; top: 112px; gap: 12px; }
  .card--back .brand__disc { width: 68px; height: 68px; }
  .card--back .brand__name { font-size: 27px; }

  .contact-panel {
    position: absolute;
    left: 206px; top: 0;
    width: 293px; height: 245px;
    background: var(--panel);
    color: var(--white);
  }
  .person__name {
    position: absolute; left: 0; right: 0; top: 38px;
    text-align: center;
    font-size: 24px; font-weight: 700;
    letter-spacing: 0.2px;
  }
  .person__role {
    position: absolute; left: 0; right: 0; top: 72px;
    text-align: center;
    font-family: "Arimo", sans-serif;
    font-size: 15px; font-weight: 400;
  }
  .contact-list { list-style: none; }
  .contact-item {
    position: absolute; left: 40px;
    height: 16px;
    display: flex; align-items: center; gap: 11px;
    font-size: 11.3px; font-weight: 500;
    letter-spacing: 0.5px;
  }
  .contact-item svg { width: 15px; height: 15px; flex: none; }
  .contact-item--phone { top: 114px; }
  .contact-item--web   { top: 143px; }
  .contact-item--mail  { top: 168px; }
  .contact-item--place { top: 194px; }
</style>
</head>
<body>

  <section class="card card--front" aria-label="Visitenkarte Vorderseite">
    <svg class="stripes" viewBox="0 0 799 456" preserveAspectRatio="none" aria-hidden="true">
      <polygon class="stripe--dark" points="0,0 107,0 57,49 0,49"/>
      <polygon class="stripe--light" points="132,0 242,0 192,49 80,49"/>
      <polygon class="stripe--dark" points="0,407 107,407 57,456 0,456"/>
      <polygon class="stripe--light" points="132,407 242,407 192,456 80,456"/>
      <polygon class="stripe--dark" points="275,407 356,407 303,456 225,456"/>
      <polygon class="stripe--light" points="356,407 467,407 416,456 303,456"/>
      <polygon class="stripe--dark" points="467,407 799,407 799,456 416,456"/>
    </svg>

    <div class="brand">
      <span class="brand__disc"></span>
      <span class="brand__name">TERRAVIA PLAN</span>
    </div>

    <div class="contact-panel">
      <h1 class="person__name">Lukas Brandtner</h1>
      <p class="person__role">CEO</p>
      <ul class="contact-list">
        <li class="contact-item contact-item--phone">
          <svg viewBox="0 0 16 16" aria-hidden="true">
            <circle cx="8" cy="8" r="6.8" fill="none" stroke="#fff" stroke-width="1.3"/>
            <path d="M5.6 4.6l1.2-.3.8 1.8-.8.7c.4.9 1.1 1.6 2 2l.7-.8 1.8.8-.3 1.2c-.2.5-.7.7-1.2.6C7.6 10.1 5.9 8.4 5.4 6.1c-.1-.6.1-1.2.2-1.5z" fill="#fff"/>
          </svg>
          <span>+12 3456 78 90</span>
        </li>
        <li class="contact-item contact-item--web">
          <svg viewBox="0 0 16 16" aria-hidden="true">
            <circle cx="8" cy="8" r="7" fill="#fff"/>
            <path d="M4 4.5c1 .3 1.5 1 1.3 2-.2.8.6 1.2 1.2 1.7.5.5.2 1.4-.3 2-.4.5-.2 1.4.3 2.4-2-.6-3.4-2.5-3.4-4.6 0-1.3.4-2.5 1.2-3.5zM9.5 2.3c.3.7.1 1.4-.5 1.8-.7.4-.4 1.2.3 1.4.9.2 1.4.9 2 1.5.5.5 1.3.4 1.8.2-.1 1.3-.7 2.5-1.6 3.4-.4-.6-1-.9-1.7-.9-.9 0-1.2-.9-.8-1.6.3-.6-.2-1.2-.9-1.3" fill="#000"/>
          </svg>
          <span>www.yourcompany.com</span>
        </li>
        <li class="contact-item contact-item--mail">
          <svg viewBox="0 0 16 16" aria-hidden="true">
            <rect x="1" y="3.5" width="14" height="9.5" fill="#fff"/>
            <path d="M1 3.5l7 5.5 7-5.5M1 13l5-4.5M15 13l-5-4.5" fill="none" stroke="#000" stroke-width="0.9"/>
          </svg>
          <span>company@email.com</span>
        </li>
        <li class="contact-item contact-item--place">
          <svg viewBox="0 0 16 16" aria-hidden="true">
            <path d="M8 1a5 5 0 0 0-5 5c0 3.6 5 9 5 9s5-5.4 5-9a5 5 0 0 0-5-5z" fill="#fff"/>
            <circle cx="8" cy="6" r="2" fill="#000"/>
          </svg>
          <span>my street 123 justice district</span>
        </li>
      </ul>
    </div>
  </section>

  <section class="card card--back" aria-label="Visitenkarte Rückseite">
    <svg class="stripes" viewBox="0 0 799 456" preserveAspectRatio="none" aria-hidden="true">
      <polygon class="stripe--dark" points="0,393 379,393 329,456 0,456"/>
      <polygon class="stripe--light" points="379,393 491,393 440,456 329,456"/>
      <polygon class="stripe--dark" points="491,393 569,393 520,456 440,456"/>
    </svg>

    <div class="brand">
      <span class="brand__disc"></span>
      <span class="brand__name">TERRAVIA PLAN</span>
    </div>
  </section>

</body>
</html>
```